Need DL Flyer for Real Estate Drops

We need a real estate flyer ,double sided. With content on 1 side like: Want to know what's your house is worth " contact us today and on other side agent details. We are looking for an ongoing partnership with designer so this assignment will be ongoing

```html
<!DOCTYPE html>
<html lang="en">
<head>
<meta charset="utf-8">
<title>Meridian Real Estate – DL Flyer</title>
<link href="https://fonts.googleapis.com/css2?family=Jost:wght@400;500;600;700&display=swap" rel="stylesheet">
<style>
  :root{
    --red:#c8102e;
    --red-deep:#a30d26;
    --navy:#1b1730;
    --white:#ffffff;
    --paper:#f7f7f7;
    --ink:#111111;
    --page-bg:#d9d9d9;
  }
  *{box-sizing:border-box;margin:0;padding:0}
  html,body{width:1200px;height:801px;overflow:hidden;background:var(--page-bg);font-family:'Jost',sans-serif}
  .spread{position:absolute;left:60px;top:40px;width:1080px;height:720px;display:flex;box-shadow:0 8px 30px rgba(0,0,0,.18)}
  .panel{position:relative;width:540px;height:720px;background:var(--paper);overflow:hidden}
  .panel svg.art{position:absolute;left:0;top:0}
  .brand{position:absolute;display:flex;flex-direction:column;align-items:flex-start;color:var(--white);font-weight:500;line-height:1}
  .brand-name{font-size:34px;letter-spacing:.5px}
  .brand-sub{font-size:9px;letter-spacing:3px;margin-top:3px;padding-left:2px}
  .brand--front{left:355px;top:70px}
  .headline{position:absolute;left:0;right:0;top:555px;text-align:center;font-weight:700;font-size:34px;line-height:1.15;letter-spacing:1.5px;color:var(--ink)}
  .cta-band{position:absolute;left:0;right:0;bottom:0;height:62px;background:var(--red);display:flex;align-items:flex-start;justify-content:center;padding-top:8px}
  .cta-text{color:var(--white);font-weight:600;font-size:15px;letter-spacing:1px}
  .agent-name{position:absolute;right:30px;top:264px;font-weight:700;font-size:32px;letter-spacing:2px;color:var(--ink);text-align:right;line-height:1.1}
  .agent-role{position:absolute;right:30px;top:306px;font-weight:600;font-size:11px;letter-spacing:.5px;color:var(--ink)}
  .contact-block{position:absolute;left:0;right:0;bottom:0;height:310px;background:var(--navy);padding:40px 30px 40px 30px;display:flex;flex-direction:column;justify-content:space-between;color:var(--white)}
  .contact-row{display:flex;align-items:center;justify-content:space-between;gap:14px}
  .contact-row--split > .contact-item{flex:0 0 50%}
  .contact-item{display:flex;align-items:center;gap:12px;font-size:13px;letter-spacing:.6px;white-space:nowrap}
  .icon{flex:0 0 30px;width:30px;height:30px;border-radius:50%;background:var(--red);display:flex;align-items:center;justify-content:center}
  .icon svg{width:15px;height:15px}
  .social{display:flex;gap:18px;flex:0 0 auto}
  .social-dot{width:30px;height:30px;border-radius:50%;background:var(--red)}
</style>
</head>
<body>
<main class="spread">

  <!-- Front: valuation offer -->
  <section class="panel panel--front">
    <svg class="art" width="540" height="720" viewBox="0 0 540 720">
      <defs>
        <linearGradient id="interiorTone" x1="0" y1="0" x2="1" y2="1">
          <stop offset="0" stop-color="#e9dcc0"/>
          <stop offset=".5" stop-color="#c9a870"/>
          <stop offset="1" stop-color="#d9d4cc"/>
        </linearGradient>
      </defs>
      <path role="img" aria-label="Photo of a bright living room with bookshelves and lounge chairs"
            d="M0 0 H540 V330 C420 420 240 470 0 470 Z" fill="url(#interiorTone)"/>
      <path class="overlay-red" d="M230 0 H540 V400 C420 385 290 250 230 0 Z" fill="var(--red)" opacity=".93"/>
      <path d="M230 0 C290 250 420 385 540 400" fill="none" stroke="var(--white)" stroke-width="12"/>
      <path d="M250 80 C330 300 440 395 540 420 V445 C420 430 300 330 250 80 Z" fill="var(--red-deep)"/>
      <path d="M0 478 H260 C170 505 80 525 0 540 Z" fill="var(--red)"/>
    </svg>
    <div class="brand brand--front">
      <span class="brand-name">meridian</span>
      <span class="brand-sub">REAL ESTATE</span>
    </div>
    <h1 class="headline">Want to know what your<br>house is worth</h1>
    <div class="cta-band"><span class="cta-text">Contact Us Today</span></div>
  </section>

  <!-- Back: agent details -->
  <section class="panel panel--back">
    <svg class="art" width="540" height="720" viewBox="0 0 540 720">
      <defs>
        <linearGradient id="houseTone" x1="0" y1="0" x2="0" y2="1">
          <stop offset="0" stop-color="#9aa7b8"/>
          <stop offset=".45" stop-color="#d8d3cc"/>
          <stop offset=".75" stop-color="#c98a4e"/>
          <stop offset="1" stop-color="#6b4a34"/>
        </linearGradient>
      </defs>
      <path role="img" aria-label="Photo of a modern single-storey home at dusk with lit windows and garden"
            d="M0 0 H470 C430 190 300 320 0 360 Z" fill="url(#houseTone)"/>
      <path d="M0 360 C300 320 430 190 470 0" fill="none" stroke="var(--red)" stroke-width="9"/>
      <path d="M0 0 H150 C110 60 60 100 0 120 Z" fill="var(--red)"/>
      <circle cx="410" cy="150" r="102" fill="var(--white)"/>
      <circle role="img" aria-label="Portrait photo of the agent" cx="410" cy="150" r="94" fill="#bdbdbd"/>
    </svg>
    <h2 class="agent-name">Arjun Malhotra</h2>
    <p class="agent-role">(Managing Director/LEA, Meridian Real Estate)</p>

    <div class="contact-block">
      <div class="contact-row">
        <div class="contact-item">
          <span class="icon"><svg viewBox="0 0 16 16"><path d="M1 4h14v9H1z" fill="none" stroke="#fff" stroke-width="1.5"/><path d="M1 4l7 5 7-5" fill="none" stroke="#fff" stroke-width="1.5"/></svg></span>
          arjun@meridianrealestate.com.au
        </div>
      </div>
      <div class="contact-row contact-row--split">
        <div class="contact-item">
          <span class="icon"><svg viewBox="0 0 16 16"><path d="M4 1l3 3-2 2c1 2 3 4 5 5l2-2 3 3-2 2C7 15 1 9 2 3z" fill="#fff"/></svg></span>
          03 9555 0142
        </div>
        <div class="contact-item">
          <span class="icon"><svg viewBox="0 0 16 16"><path d="M4 1l3 3-2 2c1 2 3 4 5 5l2-2 3 3-2 2C7 15 1 9 2 3z" fill="#fff"/></svg></span>
          0400 555 218
        </div>
      </div>
      <div class="contact-row">
        <div class="contact-item">
          <span class="icon"><svg viewBox="0 0 16 16"><circle cx="8" cy="8" r="6.5" fill="none" stroke="#fff" stroke-width="1.3"/><path d="M1.5 8h13M8 1.5c-3 3-3 10 0 13M8 1.5c3 3 3 10 0 13" fill="none" stroke="#fff" stroke-width="1.1"/></svg></span>
          https://www.meridianrealestate.com.au
        </div>
      </div>
      <div class="contact-row">
        <div class="contact-item">
          <span class="icon"><svg viewBox="0 0 16 16"><path d="M8 15s5-5.5 5-9A5 5 0 0 0 3 6c0 3.5 5 9 5 9z" fill="#fff"/><circle cx="8" cy="6" r="1.8" fill="#c8102e"/></svg></span>
          14/8 Harbour Lane, Westfield 3030
        </div>
        <div class="social" aria-label="Social media links">
          <span class="social-dot"></span>
          <span class="social-dot"></span>
        </div>
      </div>
    </div>
  </section>

</main>
</body>
</html>
```